Banner Ad for a Holding Page of a Website - Power Parcel

We require a sort of banner ad or an impactful image to use in the holding page, while we work on a final worksite, while providing basic information about the project.
In other words, a nice image instead of (or in addition to) using the boring "under construction" text.
The project is a new service, which consists of sending highly trained energy efficiency technicians to homes for a 2 hour intervention in order to help householders improve the energy efficiency of their homes. These interventions consist of adjusting the central thermostat, maybe installing thermostatic valves on the radiators, low consumption lightbulbs, etc. In addition, these technicians will also provide the householders advise for improving the energy efficiency of their homes, e.g. length of showers, more efficient ways of cooking, washing, etc. I'm attaching a couple of ideas (banner 1 & 2) that I like in terms of nice and different images for the holding page banner. Also, feel free to google the following measures we install or adjust: thermostatic radiator valves, room or central thermostats, LED lightbulbs or low consumption light bulbs. Which might trigger some nice ideas for this banner. I'm looking forward to seeing your proposals or let me know if you need further information (I'm attaching also an initial write up about the project).

March 6th:
I've just added a file with the current thinking on the holding page (including a top logo). Please note the red section, which is the specific image briefed to Sketch Plaza designers. The project is not the whole page, it is only the "under construction" image. Thanks

Target Market(s)

Mainly households interested in energy saving, due to high costs of energy, the environment or improving comfort.

Industry/Entity Type

Construction

Colors

Designer to choose colors to be used in the design.

Requirements
Must have
• Convey the idea of under construction or coming soon.
Creativity relevant to the project.

```html
<!DOCTYPE html>
<html lang="en">
<head>
<meta charset="utf-8">
<title>Power Parcel – Coming Soon</title>
<link rel="stylesheet" href="https://fonts.googleapis.com/css2?family=PT+Sans:wght@400;700&display=swap">
<style>
  :root {
    --header-bg: #f9f9f9;
    --body-bg: #ebebeb;
    --brand-blue: #1f8fc4;
    --brand-dark: #24506f;
    --intro-text: #2b6a94;
    --field-border: #dcdcdc;
    --field-text: #a4a4a4;
    --footer-bg: #2299cf;
    --footer-text: #1f2f3a;
    --white: #ffffff;
    --photo-light: #c9cde6;
    --photo-mid: #6c72a8;
    --photo-dark: #2e3160;
  }
  * { box-sizing: border-box; margin: 0; padding: 0; }
  html, body { width: 1200px; height: 950px; overflow: hidden; }
  body {
    font-family: "PT Sans", "Myriad Pro", sans-serif;
    background: var(--body-bg);
    position: relative;
  }
  .site-header {
    position: absolute; top: 0; left: 0; width: 1200px; height: 86px;
    background: var(--header-bg);
    display: flex; align-items: center; justify-content: center;
  }
  .brand {
    display: flex; align-items: center; gap: 10px;
    font-size: 38px; font-weight: 400; color: var(--brand-blue);
    letter-spacing: 0.5px;
  }
  .brand-dot {
    width: 30px; height: 30px; border-radius: 50%;
    background: var(--brand-dark);
  }
  .hero {
    position: absolute; top: 86px; left: 0; width: 1200px; height: 457px;
  }
  .hero-photo {
    position: absolute; inset: 0;
    background:
      radial-gradient(ellipse 180px 260px at 785px 230px, rgba(255,246,214,0.85), rgba(255,246,214,0) 70%),
      radial-gradient(ellipse 700px 400px at 700px 280px, var(--photo-light), rgba(201,205,230,0) 75%),
      linear-gradient(180deg, var(--photo-mid) 0%, var(--photo-dark) 100%);
  }
  .hero-title {
    position: absolute; top: 34px; left: 118px;
    font-size: 42px; font-weight: 400; color: var(--white);
    text-shadow: 0 0 14px rgba(255,255,255,0.55);
  }
  .hero-shadow {
    position: absolute; top: 543px; left: 40px; width: 1120px; height: 30px;
    background: radial-gradient(ellipse 50% 100% at 50% 0%, rgba(0,0,0,0.35), rgba(0,0,0,0) 100%);
  }
  .intro {
    position: absolute; top: 594px; left: 0; width: 1200px;
    text-align: center; font-size: 16.5px; line-height: 21px;
    color: var(--intro-text);
  }
  .signup-form {
    position: absolute; top: 676px; left: 115px; width: 990px; height: 110px;
  }
  .field {
    position: absolute; height: 42px;
    background: var(--white); border: 1px solid var(--field-border);
    font-family: inherit; font-size: 16px; color: var(--field-text);
    padding: 0 14px; display: flex; align-items: center;
  }
  .field-first { left: 0; top: 0; width: 292px; }
  .field-last { left: 0; top: 60px; width: 292px; }
  .field-email { left: 308px; top: 0; width: 292px; }
  .field-post { left: 308px; top: 60px; width: 292px; }
  .field-address { left: 615px; top: 0; width: 357px; }
  .submit-button {
    position: absolute; left: 617px; top: 62px; width: 141px; height: 40px;
    border: none; border-radius: 3px;
    background: linear-gradient(180deg, #45b3df 0%, #2291c2 55%, #17729e 100%);
    color: var(--white); font-family: inherit; font-size: 22px;
    display: flex; align-items: center; padding-left: 13px; gap: 12px;
    box-shadow: 0 6px 6px -4px rgba(0,0,0,0.35);
  }
  .site-footer {
    position: absolute; top: 813px; left: 0; width: 1200px; height: 137px;
    background: var(--footer-bg);
    border-top: 2px solid #1c7fae;
    text-align: center; color: var(--footer-text);
    font-size: 16px; line-height: 22px;
    text-shadow: 0 1px 0 rgba(255,255,255,0.45);
  }
  .contact-address { position: absolute; top: 20px; left: 0; width: 1200px; }
  .contact-line { display: inline-flex; align-items: center; gap: 8px; }
  .contact-email { position: absolute; top: 65px; left: 0; width: 1200px; }
  .footer-mark {
    position: absolute; top: 98px; left: 587px;
    width: 26px; height: 26px; border-radius: 50%;
    background: var(--brand-dark);
  }
</style>
</head>
<body>
  <header class="site-header">
    <div class="brand"><span class="brand-dot"></span>tidewell</div>
  </header>

  <section class="hero">
    <div class="hero-photo" role="img" aria-label="Photograph of many dull incandescent light bulbs lying on a blue surface, with one glowing low-energy spiral bulb standing upright among them"></div>
    <h1 class="hero-title">Save Energy Save The Future</h1>
  </section>
  <div class="hero-shadow"></div>

  <p class="intro">If you think you might be interested in learning more about this project when it gets launched, please sign up with the following form,<br>so we can send you relevant information about it:</p>

  <form class="signup-form">
    <div class="field field-first">First Name</div>
    <div class="field field-email">Email Address</div>
    <div class="field field-address">Address</div>
    <div class="field field-last">Last Name</div>
    <div class="field field-post">Post Code</div>
    <button type="button" class="submit-button">SUBMIT
      <svg width="32" height="32" viewBox="0 0 32 32" aria-hidden="true">
        <circle cx="16" cy="16" r="15" fill="#1a6f99" stroke="#7cc9ea" stroke-width="1.5"/>
        <path d="M8 13h9v-5l8 8-8 8v-5H8z" fill="#4fb6e4"/>
      </svg>
    </button>
  </form>

  <footer class="site-footer">
    <div class="contact-address">
      <span class="contact-line">
        <svg width="14" height="18" viewBox="0 0 14 18" aria-hidden="true">
          <path d="M7 0C3.1 0 0 3.1 0 7c0 5 7 11 7 11s7-6 7-11c0-3.9-3.1-7-7-7z" fill="#7fd3f5"/>
          <circle cx="7" cy="7" r="2.6" fill="#2299cf"/>
        </svg>
        The Grain Loft,
      </span><br>
      Harbour Walk, Bristol, BS2 4QT
    </div>
    <div class="contact-email">
      <span class="contact-line">
        <svg width="18" height="12" viewBox="0 0 18 12" aria-hidden="true">
          <rect width="18" height="12" fill="#9fdcf5"/>
          <path d="M0 0l9 7 9-7" fill="none" stroke="#2299cf" stroke-width="1.5"/>
        </svg>
        &nbsp;info@power-parcel.com
      </span>
    </div>
    <div class="footer-mark"></div>
  </footer>
</body>
</html>
```